Interior designer needs a gorgeous, chic business card design.

A new, small Interior Design firm needs a business card that is chic, contemporary and elegant. Nothing over the top. My interiors are contemporary classic with an elegant feel to them. I like to use quality finishes and products rather than follow the latest fads. Projects can be anything from Pre start selections, bathrooms, kitchens, bedrooms, custom upholstery, furniture, rugs and art etc. The final design should display quality and an achievable sense of chic. I am open to all colours including black but not limited to this.

Business

```html
<!DOCTYPE html>
<html lang="en">
<head>
<meta charset="utf-8">
<title>Hollis Interiors — Business Card</title>
<link href="https://fonts.googleapis.com/css2?family=Marcellus&display=swap" rel="stylesheet">
<style>
  :root {
    --backdrop: #e9e7e4;
    --card-black: #0b0b0b;
    --card-sheen: #262626;
    --ink-white: #f4f4f2;
    --tile-border: #1a1a1a;
  }
  * { margin: 0; padding: 0; box-sizing: border-box; }
  html, body {
    width: 1200px;
    height: 1024px;
    overflow: hidden;
    background: var(--backdrop);
  }
  .canvas {
    position: relative;
    width: 1200px;
    height: 1024px;
    display: flex;
    align-items: center;
    justify-content: center;
  }
  .business-card {
    position: relative;
    width: 1000px;
    height: 572px;
    background: linear-gradient(120deg, var(--card-black) 0%, var(--card-sheen) 38%, var(--card-black) 62%, var(--card-black) 100%);
    box-shadow: 0 18px 40px rgba(0,0,0,0.25);
    overflow: hidden;
  }
  .brand-name {
    position: absolute;
    left: 70px;
    top: 120px;
    font-family: "Marcellus", serif;
    font-weight: 400;
    font-size: 76px;
    line-height: 1;
    letter-spacing: 0.06em;
    color: var(--ink-white);
    white-space: nowrap;
  }
  .portfolio-strip {
    position: absolute;
    left: 70px;
    right: 40px;
    bottom: 40px;
    height: 180px;
    display: grid;
    grid-template-columns: repeat(4, 1fr);
    gap: 18px;
  }
  .portfolio-tile {
    border: 4px solid var(--tile-border);
    box-shadow: 0 0 0 1px rgba(255,255,255,0.08);
  }
  .tile-living { background: linear-gradient(135deg, #cfd0c8, #9aa08f 60%, #e3e1d6); }
  .tile-studio { background: linear-gradient(135deg, #e4e4e4, #a9a9ab 55%, #d6d6d6); }
  .tile-stair { background: linear-gradient(135deg, #e8d6bf, #9c6f4c 55%, #d9c4a6); }
  .tile-lounge { background: linear-gradient(135deg, #d7d7db, #9e9aa8 55%, #e6e4ea); }
</style>
</head>
<body>
  <main class="canvas">
    <section class="business-card">
      <h1 class="brand-name">Hollis Interiors</h1>
      <div class="portfolio-strip">
        <div class="portfolio-tile tile-living" role="img" aria-label="Photo of a bright living room with sofa and green accents"></div>
        <div class="portfolio-tile tile-studio" role="img" aria-label="Photo of a white interior with dark feature artwork"></div>
        <div class="portfolio-tile tile-stair" role="img" aria-label="Photo of a warm hallway with timber staircase and wall art"></div>
        <div class="portfolio-tile tile-lounge" role="img" aria-label="Photo of a soft lilac lounge with cushions"></div>
      </div>
    </section>
  </main>
</body>
</html>
```